Nutrition Company seeks label design for new product line CHIA Seeds TEA

Vembra Nutrition focuses on bringing natural nutritional/dietary supplements to the world.
We need a label design for a new product we are creating by combining instant tea granulate with organic chia seeds.  We have three flavors for introduction and will be adding more as the formulas are created.  The first three will be Ginger Tea, Harbor Tea, Cleansing Tea.
Exact nutritional facts are still being worked on and will be updated as it becomes available.  Ginger Tea nutritional facts is available.
Attached are files of label specification, samples that we like for you to use as inspirational ideas, a label of one of our product, logo (you are free to change the logo text style), and a product that uses the same container the label will be placed on.

Updates
White Wide Mouth Jar png file has been added for designers who wants to use it.  Product specification for ginger has been updated fixing minor grammatical errors.

Reason: Due to the holiday weekend, deadline has been extended so designers can enjoy the holiday.  Payment will be set to guaranteed.  Thank you for all who have submitted their designs.  Those who haven't submitted yet, please do!  We are eager to see your creativity and may use designs for future product lines.

If you are using a stock image please let us know.  We will look into the cost of paying for the stock image license rights to be used.  Thank you.

Target Market(s)
Health conscious individuals. Ages 25 - 60.
Industry/Entity Type
It Company
Requirements
Must have
- Final design must be print ready AI file with bleed.  And white plates if needed.

Nice to have
- "Chia Tea" in a fixed location with flavor, like Plomi Twist example in Chia Tea Sample document.
Refer to Chia Tea Samples document.

```html
<!DOCTYPE html>
<html lang="en">
<head>
<meta charset="utf-8">
<title>Vembra Nutrition – Chia Tea Labels</title>
<link href="https://fonts.googleapis.com/css2?family=Oswald:wght@500;600&family=Open+Sans:wght@600;700&family=Roboto+Condensed:wght@700&display=swap" rel="stylesheet">
<style>
  :root {
    --bg-top: #e9eaeb;
    --bg-bottom: #c9cbcf;
    --label: #ffffff;
    --brand-green: #4a8a3b;
    --leaf-green: #5a9a48;
    --chia-purple: #6c5aa9;
    --ink: #1c1c1c;
    --ginger: #c99a5a;
    --ginger-art: #e3d27e;
    --harbor: #8a1b4f;
    --harbor-art: #c78ea8;
    --cleansing: #e0632a;
    --cleansing-art: #e89a66;
    --cleansing-art-2: #8fa46a;
    --badge: #3a3a44;
    --badge-inner: #d9c56a;
  }
  * { margin: 0; padding: 0; box-sizing: border-box; }
  html, body { width: 1200px; height: 678px; overflow: hidden; }
  body {
    background: linear-gradient(var(--bg-top), var(--bg-bottom));
    position: relative;
    font-family: "Open Sans", sans-serif;
  }
  .label {
    position: absolute;
    top: 250px;
    width: 290px;
    height: 210px;
    background: var(--label);
    overflow: hidden;
    box-shadow: 0 6px 18px rgba(0,0,0,0.18);
  }
  .label--ginger { left: 127px; }
  .label--harbor { left: 456px; }
  .label--cleansing { left: 785px; }

  .brand-panel {
    position: absolute;
    top: 0; left: 50%;
    transform: translateX(-50%);
    width: 124px; height: 56px;
    background: var(--brand-green);
    display: flex; align-items: center; justify-content: center; gap: 7px;
  }
  .brand-dot {
    width: 14px; height: 14px; border-radius: 50%;
    background: #ffffff;
  }
  .brand-name {
    color: #ffffff;
    font-weight: 700;
    font-size: 11.5px;
    line-height: 1.05;
    text-transform: uppercase;
  }
  .product-line {
    position: absolute;
    top: 58px; left: 0; right: 0;
    display: flex; align-items: center; justify-content: center; gap: 4px;
    font-family: "Oswald", sans-serif;
    font-weight: 600;
    font-size: 29px;
    color: var(--chia-purple);
    line-height: 1.1;
  }
  .product-line__tea { font-weight: 500; }
  .leaf-mark {
    display: inline-block;
    width: 24px; height: 16px;
    border-radius: 50% 50% 45% 45%;
    background: radial-gradient(ellipse at center, var(--leaf-green) 55%, rgba(90,154,72,0) 75%);
  }
  .flavor {
    position: absolute;
    top: 94px; left: 0; right: 0;
    text-align: center;
    font-weight: 700;
    font-size: 16.5px;
    color: var(--ink);
  }
  .claim {
    position: absolute;
    top: 112px;
    font-family: "Roboto Condensed", sans-serif;
    font-weight: 700;
    font-size: 12px;
    line-height: 1.25;
    color: var(--chia-purple);
    text-align: center;
  }
  .claim--organic { left: 6px; width: 84px; }
  .claim--servings { right: 6px; width: 84px; }

  .flavor-art {
    position: absolute;
    top: 116px; left: 50%;
    transform: translateX(-50%);
    width: 96px; height: 52px;
  }
  .label--ginger .flavor-art {
    background: radial-gradient(ellipse 50% 50% at 50% 55%, var(--ginger-art) 45%, rgba(227,210,126,0) 100%);
  }
  .label--harbor .flavor-art {
    background: radial-gradient(ellipse 45% 50% at 50% 50%, var(--harbor-art) 45%, rgba(199,142,168,0) 100%);
  }
  .label--cleansing .flavor-art {
    background:
      radial-gradient(ellipse 30% 40% at 35% 60%, var(--cleansing-art) 40%, rgba(232,154,102,0) 100%),
      radial-gradient(ellipse 30% 40% at 68% 45%, var(--cleansing-art-2) 40%, rgba(143,164,106,0) 100%);
  }

  .base-band {
    position: absolute;
    left: 0; bottom: 0;
    width: 290px; height: 48px;
  }
  .net-weight {
    position: absolute;
    bottom: 10px; left: 0; right: 0;
    text-align: center;
    font-weight: 700;
    font-size: 14px;
  }
  .label--ginger .net-weight { color: var(--ink); }
  .label--harbor .net-weight,
  .label--cleansing .net-weight { color: #ffffff; }

  .guarantee-badge {
    position: absolute;
    right: 10px; bottom: 6px;
    width: 52px; height: 52px;
    border-radius: 50%;
    background: var(--badge);
    border: 3px solid #ffffff;
    box-shadow: 0 1px 3px rgba(0,0,0,0.35);
  }
  .guarantee-badge::after {
    content: "";
    position: absolute;
    inset: 10px;
    border-radius: 50%;
    background: var(--badge-inner);
  }
</style>
</head>
<body>

  <section class="label label--ginger">
    <div class="brand-panel"><span class="brand-dot"></span><span class="brand-name">Vembra<br>Nutrition</span></div>
    <h1 class="product-line"><span>CHIA</span><span class="leaf-mark" role="img" aria-label="Small leaf sprig"></span><span class="product-line__tea">TEA</span></h1>
    <h2 class="flavor">Ginger</h2>
    <p class="claim claim--organic">Certified Organic<br>Chia seeds</p>
    <p class="claim claim--servings">20 Servings<br>per Container</p>
    <div class="flavor-art" role="img" aria-label="Illustration of ginger root"></div>
    <svg class="base-band" viewBox="0 0 290 48" preserveAspectRatio="none" aria-hidden="true">
      <path d="M0 8 C20 0 40 0 60 8 S100 16 120 8 S160 0 180 8 S220 16 240 8 S275 0 290 6 V48 H0 Z" fill="var(--ginger)"/>
    </svg>
    <p class="net-weight">Net wt. 250g</p>
    <div class="guarantee-badge"></div>
  </section>

  <section class="label label--harbor">
    <div class="brand-panel"><span class="brand-dot"></span><span class="brand-name">Vembra<br>Nutrition</span></div>
    <h1 class="product-line"><span>CHIA</span><span class="leaf-mark" role="img" aria-label="Small leaf sprig"></span><span class="product-line__tea">TEA</span></h1>
    <h2 class="flavor">Harbor</h2>
    <p class="claim claim--organic">Certified Organic<br>Chia seeds</p>
    <p class="claim claim--servings">20 Servings<br>per Container</p>
    <div class="flavor-art" role="img" aria-label="Illustration of a pink flavor ingredient"></div>
    <svg class="base-band" viewBox="0 0 290 48" preserveAspectRatio="none" aria-hidden="true">
      <path d="M0 8 C20 0 40 0 60 8 S100 16 120 8 S160 0 180 8 S220 16 240 8 S275 0 290 6 V48 H0 Z" fill="var(--harbor)"/>
    </svg>
    <p class="net-weight">Net wt. 250g</p>
    <div class="guarantee-badge"></div>
  </section>

  <section class="label label--cleansing">
    <div class="brand-panel"><span class="brand-dot"></span><span class="brand-name">Vembra<br>Nutrition</span></div>
    <h1 class="product-line"><span>CHIA</span><span class="leaf-mark" role="img" aria-label="Small leaf sprig"></span><span class="product-line__tea">TEA</span></h1>
    <h2 class="flavor">Cleansing</h2>
    <p class="claim claim--organic">Certified Organic<br>Chia seeds</p>
    <p class="claim claim--servings">20 Servings<br>per Container</p>
    <div class="flavor-art" role="img" aria-label="Illustration of flowing orange and green swirls"></div>
    <svg class="base-band" viewBox="0 0 290 48" preserveAspectRatio="none" aria-hidden="true">
      <path d="M0 8 C20 0 40 0 60 8 S100 16 120 8 S160 0 180 8 S220 16 240 8 S275 0 290 6 V48 H0 Z" fill="var(--cleansing)"/>
    </svg>
    <p class="net-weight">Net wt. 250g</p>
    <div class="guarantee-badge"></div>
  </section>

</body>
</html>
```